I am looking for a book cover designs. The title of the book is "Why some rooms go quiet and what you can change about it"

the book is not too formal but it is also not informal.

I wish for the title to be easily readable and capturing, especially the "why some rooms go quiet" part.

the book should also include the author name: Teodor Vasko

Target Market(s)

everyone

Requirements
Must have
• Full title and author name: Teodor Vasko
Nice to have
• There is a chapter that is called "sit with the mirror", if you wish to do an illustration as part of the cover then perhaps that can give you an idea of what to go with.
Should not have
• anything that takes attention away from the title.Also should not include any photographs.

```html
<!DOCTYPE html>
<html lang="en">
<head>
<meta charset="utf-8">
<title>Why some rooms go quiet — Teodor Vasko</title>
<link rel="stylesheet" href="https://fonts.googleapis.com/css2?family=Bebas+Neue&family=PT+Serif:wght@700&display=swap">
<style>
  :root {
    --ink: #231f20;
    --paper: #ffffff;
  }
  html, body {
    margin: 0;
    padding: 0;
    overflow: hidden;
    background: var(--paper);
  }
  .cover {
    position: relative;
    width: 1200px;
    height: 663px;
    background: var(--paper);
    overflow: hidden;
  }
  .cover__art {
    display: block;
    width: 1200px;
    height: 663px;
  }
  .title-main {
    font-family: "Bebas Neue", "Oswald", sans-serif;
    font-size: 190px;
    letter-spacing: 2px;
    fill: var(--ink);
  }
  .title-sub {
    font-family: "PT Serif", Georgia, serif;
    font-weight: 700;
    font-size: 54px;
    fill: var(--ink);
  }
  .author {
    font-family: "PT Serif", Georgia, serif;
    font-weight: 700;
    font-size: 30px;
    letter-spacing: 3px;
    fill: var(--ink);
  }
</style>
</head>
<body>
  <main class="cover">
    <svg class="cover__art" viewBox="0 0 1200 663" xmlns="http://www.w3.org/2000/svg" role="img" aria-label="Why some rooms go quiet and what you can change about it, by Teodor Vasko">
      <text class="title-main" x="600" y="261" text-anchor="middle" textLength="880" lengthAdjust="spacingAndGlyphs">WHY SOME ROOMS</text>
      <text class="title-main" x="600" y="428" text-anchor="middle">GO QUIET</text>
      <text class="title-sub" x="600" y="498" text-anchor="middle">and what you can change about it</text>
      <text class="author" x="600" y="590" text-anchor="middle">Teodor Vasko</text>
    </svg>
  </main>
</body>
</html>
```